Vortique Energy Business Card Design

website: www.vortiqueenergy.example
Project: Business Card Design for Vortique Energy
Name: Derek Holloway
Title: Founder / Operations Strategist
Visual Identity & Logo:
Logo File: VRT-Logo-FullGradient-Final.png (Attached).
Color Palette: The brand relies on a distinctive Cyan (Blue) to Lime Green gradient.
Background Preference: We want a Dark Mode aesthetic (Deep Matte Black, Charcoal, or Dark Slate) to make the neon gradient of the logo pop. This feels more "tech/industrial" than a standard white card.
Design Aesthetic (The "Ops" Vibe):
Concept: "Grid & Infrastructure." We are a solar rental company, focusing on logistics and access.
Typography: White, bold sans-serif text for contact info. High contrast against the dark background.
Accents: Use the Cyan or Lime Green from the logo for thin divider lines or edge painting.
Avoid: No orange/gold (clashes with logo). No cartoon leaves.
Layout Requirements:
Front: Large, centered logo. Maybe a subtle UV gloss spot varnish over the logo icon.
Back: Name, Title, Contact Info.
Texture: Matte finish cardstock with gloss elements.
sample mock up of information on card: https://brimtolcorp-my.filedock.example/:i:/g/personal/derek_holloway_vortiqueenergy_com/AbCdEfGhIjKlMnOpQrStUvWxYz0123456789AbCdEfGh?e=X1Y2Z3
Logo: https://brimtolcorp.filedock.example/:i:/s/VortiqueEnergy/ZyXwVuTsRqPoNmLkJiHgFeDcBa9876543210ZyXwVuTs?e=Q4R5S6

```html
<!DOCTYPE html>
<html lang="en">
<head>
<meta charset="utf-8">
<title>Vortique Energy Business Card</title>
<link href="https://fonts.googleapis.com/css2?family=Poppins:wght@300;400;500;600&display=swap" rel="stylesheet">
<style>
  :root {
    --backdrop: #18181b;
    --card-front: #1e1f21;
    --card-back: #232527;
    --panel-shade: #2a2c2e;
    --cyan: #22b8d6;
    --lime: #a6d13a;
    --white: #f2f2f2;
    --grey: #8d8f92;
    --silver: #b9bbbe;
  }
  * { box-sizing: border-box; margin: 0; padding: 0; }
  html, body { width: 1200px; height: 801px; overflow: hidden; }
  body {
    background: var(--backdrop);
    font-family: "Poppins", sans-serif;
    color: var(--white);
    position: relative;
  }
  .card {
    position: absolute;
    top: 246px;
    width: 540px;
    height: 309px;
    border-radius: 4px;
    overflow: hidden;
  }
  .card--front { left: 40px; background: var(--card-front); }
  .card--back { left: 620px; background: var(--card-back); }

  /* Front */
  .front-brand {
    position: absolute;
    left: 0; right: 0; top: 108px;
    display: flex; align-items: center; justify-content: center; gap: 14px;
  }
  .front-brand__mark { width: 34px; height: 34px; background: #0d0d0e; border-radius: 3px; }
  .front-brand__name { font-size: 38px; font-weight: 300; color: var(--silver); letter-spacing: 1px; }
  .front-tagline {
    position: absolute; left: 0; right: 0; top: 176px;
    text-align: center; font-size: 12px; font-weight: 400; color: var(--silver); letter-spacing: .5px;
  }

  /* Back */
  .back-panel {
    position: absolute; right: 0; top: 0; width: 250px; height: 150px;
    background: linear-gradient(135deg, var(--panel-shade), transparent 80%);
  }
  .back-brand {
    position: absolute; right: 28px; top: 34px;
    display: flex; align-items: center; gap: 9px;
  }
  .back-brand__mark { width: 18px; height: 18px; background: var(--cyan); border-radius: 2px; }
  .back-brand__name { font-size: 22px; font-weight: 400; color: var(--cyan); }
  .back-tagline {
    position: absolute; right: 28px; top: 66px;
    font-size: 7.5px; color: var(--white); letter-spacing: .3px;
  }
  .offices {
    position: absolute; right: 28px; top: 104px;
    display: flex; align-items: center; gap: 8px;
  }
  .offices__label { font-size: 11px; color: var(--white); margin-right: 2px; }
  .offices__badge { width: 26px; height: 26px; border-radius: 50%; background: #c9c9cc; }
  .offices__badge--red { background: #d8414a; }
  .offices__badge--navy { background: #3a4b8c; }

  .person { position: absolute; left: 30px; top: 40px; }
  .person__name {
    font-size: 22px; font-weight: 600;
    background: linear-gradient(90deg, var(--cyan), var(--lime));
    -webkit-background-clip: text; background-clip: text; color: transparent;
  }
  .person__title { font-size: 11.5px; font-weight: 400; margin-top: 2px; }

  .address { position: absolute; left: 30px; top: 118px; font-size: 11px; line-height: 1.4; }
  .address__company { font-weight: 600; }

  .contacts { position: absolute; left: 30px; top: 178px; list-style: none; font-size: 11px; line-height: 1.55; }
  .contacts li { display: flex; align-items: center; gap: 8px; }
  .contacts svg { width: 11px; height: 11px; flex: none; }

  .promise {
    position: absolute; left: 30px; right: 30px; top: 252px;
    font-size: 12.5px; font-weight: 400; text-align: right;
  }
  .divider {
    position: absolute; left: 30px; right: 30px; top: 276px; height: 1.5px;
    background: linear-gradient(90deg, var(--cyan), var(--lime));
  }
</style>
</head>
<body>
  <section class="card card--front" aria-label="Card front">
    <div class="front-brand">
      <span class="front-brand__mark"></span>
      <span class="front-brand__name">Vortique Energy</span>
    </div>
    <p class="front-tagline">Rent Solar. Generate Power. Save Smarter</p>
  </section>

  <section class="card card--back" aria-label="Card back">
    <div class="back-panel"></div>
    <div class="back-brand">
      <span class="back-brand__mark"></span>
      <span class="back-brand__name">Vortique Energy</span>
    </div>
    <p class="back-tagline">Rent Solar. Generate Power. Save Smarter</p>

    <div class="offices">
      <span class="offices__label">Office</span>
      <span class="offices__badge offices__badge--navy" role="img" aria-label="Office country badge"></span>
      <span class="offices__badge offices__badge--red" role="img" aria-label="Office country badge"></span>
      <span class="offices__badge offices__badge--navy" role="img" aria-label="Office country badge"></span>
    </div>

    <div class="person">
      <h1 class="person__name">Derek Holloway</h1>
      <p class="person__title">Founder / Operations Strategist</p>
    </div>

    <address class="address" style="font-style:normal">
      <div class="address__company">Vortique Energy, LLC</div>
      <div>1458 Cedar Ridge Avenue</div>
      <div>Brookfield, FL 30000</div>
    </address>

    <ul class="contacts">
      <li><svg viewBox="0 0 12 12"><rect x="1.5" y="1.5" width="9" height="9" fill="none" stroke="#22b8d6" stroke-width="1.5"/></svg>555.014.2290</li>
      <li><svg viewBox="0 0 12 12"><rect x="1" y="2.5" width="10" height="7" fill="#7cc69a"/><path d="M1 2.5 6 7 11 2.5" fill="none" stroke="#232527" stroke-width="1"/></svg>info@vortiqueenergy.example</li>
      <li><svg viewBox="0 0 12 12"><circle cx="6" cy="6" r="5" fill="#8bbf5a"/><path d="M1 6h10M6 1v10" stroke="#232527" stroke-width=".8"/></svg>www.vortiqueenergy.example</li>
    </ul>

    <p class="promise">No debt, No liens, No maintenance, Just savings</p>
    <div class="divider"></div>
  </section>
</body>
</html>
```